Brochure Design Project

TGRP
The brochure is intended to be on Tarlow Guild of Restorative Practice website available for the members to download for the purpose of educating public about benefits of clinical hypnosis and introduce it as possible treatment option. There should be a empty space left on the last page for the member to stamp their office information.
So, the intended audience is general public that might be interested in hypnosis treatment
White on blue is logo of TGRP.
I would like the brochure to have bright complimentary colors with imagery that is used in health care/complimentary medicine - nature, relaxation, etc.
TGRP website is TGRPx.net.

```html
<!DOCTYPE html>
<html lang="en">
<head>
<meta charset="utf-8">
<title>Clinical Hypnosis Brochure Spread</title>
<link rel="stylesheet" href="https://fonts.googleapis.com/css2?family=Open+Sans:wght@700&family=PT+Sans+Narrow&family=Source+Sans+3:ital,wght@0,400;0,600;0,700;1,700&display=swap">
<style>
  :root {
    --paper: #dde2ef;
    --brand-blue: #1c6db5;
    --headline-blue: #1b6cb7;
    --ink: #1f1f24;
    --white: #ffffff;
  }
  * { box-sizing: border-box; margin: 0; padding: 0; }
  html, body { width: 1200px; height: 848px; overflow: hidden; background: var(--paper); }
  body { font-family: "Source Sans 3", Arial, sans-serif; color: var(--ink); }

  .spread { position: relative; width: 1200px; height: 848px; overflow: hidden; background: var(--paper); }

  .visual { position: absolute; }
  .visual--portrait { left: 0; top: 0; width: 415px; height: 554px;
    background: linear-gradient(160deg, #f4f2f0 0%, #d9c2b0 40%, #a07e62 70%, #cfd4df 100%); }
  .visual--staircase { left: 418px; top: 0; width: 425px; height: 413px;
    background: radial-gradient(circle at 52% 48%, #fbf7f1 0%, #e0d2c0 30%, #6e6257 62%, #2b2624 100%); }
  .visual--brain { left: 845px; top: 0; width: 355px; height: 277px;
    background: radial-gradient(circle at 45% 40%, #7cc6ff 0%, #2f6fd6 45%, #122e8a 100%); }
  .visual--gears { left: 1071px; top: 406px; width: 129px; height: 194px;
    background: radial-gradient(circle at 60% 50%, #8fb4d8 0%, #c9d6e6 60%, var(--paper) 100%); }
  .visual--heads { left: 424px; top: 649px; width: 133px; height: 199px;
    background: linear-gradient(180deg, var(--paper) 0%, #b9bcc3 45%, #6f7277 100%); }
  .visual--chess { left: 856px; top: 671px; width: 132px; height: 177px;
    background: linear-gradient(135deg, #4a4a4a 0%, #1a1a1a 60%, #0a0a0a 100%); }

  .banner { position: absolute; background: var(--brand-blue); color: var(--white);
    font-family: "Open Sans", Arial, sans-serif; font-weight: 700; display: flex; align-items: center; }
  .banner--what { left: 148px; top: 138px; width: 267px; height: 72px; font-size: 35px;
    justify-content: flex-end; padding-right: 20px;
    clip-path: polygon(0 0, 100% 0, 100% 100%, 14% 100%, 18% 55%); }
  .banner--why { left: 459px; top: 41px; width: 384px; height: 70px; font-size: 34px;
    justify-content: flex-end; padding-right: 12px;
    clip-path: polygon(0 0, 100% 0, 100% 100%, 10% 100%); }
  .banner--when { left: 997px; top: 178px; width: 203px; height: 57px; font-size: 33px;
    justify-content: flex-end; padding-right: 14px;
    clip-path: polygon(0 0, 100% 0, 100% 100%, 30% 100%); }
  .banner--how { left: 845px; top: 612px; width: 272px; height: 59px; font-size: 34px;
    padding-left: 24px;
    clip-path: polygon(0 0, 100% 0, 82% 100%, 0 100%); }

  .copy { position: absolute; font-size: 11.6px; line-height: 14.2px; }
  .lead-word { font-size: 26px; font-weight: 700; color: var(--headline-blue); line-height: 1; }

  /* What it is */
  .copy--what { left: 18px; top: 566px; width: 372px; }
  .copy--what p { margin-bottom: 9px; }
  .copy--what .wrap-top { float: right; width: 0; height: 150px; }
  .copy--what .wrap-box { float: right; clear: right; width: 214px; height: 140px; }
  .copy--what .note { margin-top: 14px; text-align: justify; }

  .not-box { position: absolute; left: 182px; top: 717px; width: 233px; height: 131px;
    background: var(--brand-blue); color: var(--white); padding: 6px 15px; }
  .not-box h2 { font-size: 28px; font-weight: 600; line-height: 34px; margin-bottom: 1px; }
  .not-box li { list-style: none; font-family: "PT Sans Narrow", Arial, sans-serif;
    font-size: 11.5px; line-height: 11.5px; margin-bottom: 6px; }

  /* Why use hypnosis */
  .copy--why { left: 445px; top: 417px; width: 368px; font-size: 12.3px; line-height: 14.1px; text-align: justify; }
  .copy--why p { margin-bottom: 10px; }
  .copy--why-side { left: 445px; top: 503px; width: 143px; font-size: 12.3px; line-height: 14.1px; text-align: justify; }
  .copy--why-side p { margin-bottom: 14px; }

  .pull-quote { position: absolute; left: 597px; top: 507px; width: 249px; height: 146px;
    background: var(--brand-blue); color: var(--white); padding: 9px 31px 8px 25px;
    font-size: 15.5px; font-weight: 700; font-style: italic; line-height: 24px;
    text-align: justify; text-align-last: left; word-spacing: 2px; }

  .copy--process { left: 563px; top: 657px; width: 252px; font-size: 12.3px; line-height: 14.1px; text-align: justify; }
  .copy--process .wrap-heads { float: left; width: 120px; height: 190px;
    shape-outside: polygon(0 0, 0 28px, 90px 28px, 104px 42px, 120px 56px, 120px 190px, 0 190px); }

  /* When */
  .copy--when { left: 870px; top: 280px; width: 400px; white-space: nowrap; line-height: 14px; }
  .copy--when .lead-word { font-size: 31px; }
  .apps-title { position: absolute; left: 870px; top: 345px; font-size: 17.5px; font-weight: 700; color: var(--headline-blue); }
  .apps-list { position: absolute; left: 884px; top: 368px; width: 260px; list-style: none;
    font-size: 11.6px; line-height: 12.6px; z-index: 1; }
  .apps-list li { margin-bottom: 7.4px; white-space: nowrap; }

  /* How */
  .copy--how { left: 992px; top: 671px; width: 236px; font-size: 11px; line-height: 12.7px; text-align: justify; }
  .copy--how p { margin-bottom: 8px; }
  .copy--how em { color: var(--headline-blue); font-weight: 700; }
</style>
</head>
<body>
<main class="spread">

  <div class="visual visual--portrait" role="img" aria-label="Photo of a young woman watching a swinging pendulum held above her"></div>
  <h2 class="banner banner--what">What it is</h2>
  <div class="copy copy--what">
    <div class="wrap-top"></div>
    <div class="wrap-box"></div>
    <p><span class="lead-word">Hypnosis</span> is considered to be a state of focused attention and inner absorption; there is decreased awareness of surroundings and increased ability to respond to acceptable suggestions.</p>
    <p>A collaborative process that helps a person’s mind and body function more comfortably and effectively.</p>
    <p>It is not uncommon for all of us to experience a situation when we are so preoccupied with a thought or experience that we neglect surroundings. Examples – watching a favorite show, computer games or driving under ‘highway” hypnosis.</p>
    <p class="note">It requires special training to use hypnosis appropriately in medicine, dentistry and psychotherapy and should be done by licensed</p>
  </div>
  <aside class="not-box">
    <h2>What it is not</h2>
    <ul>
      <li>It is not a mind control, just a suggestion.</li>
      <li>It cannot be imposed on an unwilling or uninterested person</li>
      <li>It is not a miracle or cure, but a way to solve some problems.</li>
    </ul>
  </aside>

  <div class="visual visual--staircase" role="img" aria-label="Photo looking up a spiral staircase with black railings"></div>
  <h2 class="banner banner--why">Why use hypnosis</h2>
  <div class="copy copy--why">
    <p>Hypnosis is unique in its ability to help you unlock imagination, bypass the “can never happen” censor of the conscious mind, and simply help one see experiences and memories in a different light.</p>
    <p>It can help find solutions and resolutions to a difficult mental</p>
  </div>
  <div class="copy copy--why-side">
    <p>or physical problem, and find inner sources of strength and resilience.</p>
    <p>It can help a person better understand one’s own as well as others’ motivations and behavior.</p>
  </div>
  <blockquote class="pull-quote">It allows a person to choose and develop abilities and capacities that can help achieve a desired goal.</blockquote>
  <div class="visual visual--heads" role="img" aria-label="Illustration of two grey mannequin heads facing each other, joined by a cable"></div>
  <p class="copy copy--process"><span class="wrap-heads"></span>During the process of hypnosis a person is frequently taught how use individualized cues and techniques to achieve desired result (decrease anxiety, reduce pain, improve sport performance, etc.) With practice, a person can achieve a level of control that seemed impossible before.</p>

  <div class="visual visual--brain" role="img" aria-label="Illustration of a glowing blue brain with a red puzzle piece"></div>
  <h2 class="banner banner--when">When</h2>
  <p class="copy copy--when"><span class="lead-word">Hypnosis</span> has been found to be very effective for<br>treating many mental and physical conditions, as well improving<br>physical and mental performance, and changing undesirable habits.</p>
  <h3 class="apps-title">Its applications can include:</h3>
  <div class="visual visual--gears" role="img" aria-label="Illustration of a head made of blue gears held on an open hand"></div>
  <ul class="apps-list">
    <li>anxiety disorders;</li>
    <li>coping with emotional and physical trauma;</li>
    <li>insomnia;</li>
    <li>acute and chronic pain relief;</li>
    <li>preparation for surgical procedures;</li>
    <li>Childbirth;</li>
    <li>Decreasing side effects<br>of chemotherapy and radiation;</li>
    <li>gastrointestinal disorders;</li>
    <li>asthma;</li>
    <li>sports performance and tests preparation;</li>
    <li>fear of flying and</li>
    <li>smoking cessation andweight control</li>
  </ul>
  <h2 class="banner banner--how">HOW</h2>
  <div class="visual visual--chess" role="img" aria-label="Dark photo of a man behind a chess king piece"></div>
  <div class="copy copy--how">
    <p>A person conducting hypnosis will walk you through the process, help define goals and expectations, and explain how you can achieve the results you want.</p>
    <p><em>Hypnosis starts with an induction process</em> where you simply concentrate on an object, image or symbol. Induction is followed by relaxed communication and crafting of suggestion. The last step is reorientation, discussion of the experience, and instructions on home practice. All hypnosis is ultimately a form of self hypnosis.</p>
  </div>

</main>
</body>
</html>
```